Moravel Swim Stationary

Recently established Aquatics Club, with competitive swimming being a principal activity needs stationary, including business cards, letterhead and envelopes, application forms.
The designs shold incorporate the Club's logo. ( The colours are aqua and teal)
The statonary should be fun yet project a corporate image sufficient to attract potential sponsors.

Club members, sponsors, professional organisations.

Business

• Club Logo
Address & Telephone number

The letterhead must contain the Club's Mission Statement.
It can be incorporated in the "footer" on the page.

To provide aquatics programmes, for persons of all ages, that encourage physical fitness and wellness, build character and self-discipline, inspire camaraderie and promote civic mindedness and excellence.

```html
<!DOCTYPE html>
<html lang="en">
<head>
<meta charset="UTF-8">
<title>Moravel Swim — Envelope</title>
<link href="https://fonts.googleapis.com/css2?family=Lato:wght@400;700&display=swap" rel="stylesheet">
<style>
  :root {
    --backdrop: #e6e4df;
    --paper: #ffffff;
    --teal: #0b7f76;
    --orange: #d9691f;
    --ink: #3a3a3a;
  }
  html, body {
    margin: 0;
    padding: 0;
    width: 1200px;
    height: 720px;
    overflow: hidden;
    background: var(--backdrop);
    font-family: "Lato", Arial, sans-serif;
  }
  .canvas {
    position: relative;
    width: 1200px;
    height: 720px;
  }
  .envelope {
    position: absolute;
    left: 50px;
    top: 121px;
    width: 1100px;
    height: 478px;
    background: var(--paper);
    box-shadow: 0 6px 18px rgba(0,0,0,0.18);
    overflow: hidden;
  }
  .return-address {
    position: absolute;
    left: 62px;
    top: 44px;
  }
  .club-name {
    display: flex;
    align-items: center;
    gap: 10px;
    margin: 0 0 14px;
    font-size: 30px;
    font-weight: 700;
    color: var(--orange);
    letter-spacing: 0.5px;
  }
  .club-name__dot {
    width: 16px;
    height: 16px;
    border-radius: 50%;
    background: var(--teal);
  }
  .address {
    margin: 0;
    font-size: 13px;
    font-weight: 400;
    line-height: 1.35;
    color: var(--ink);
    font-style: normal;
  }
  .footer-swoosh {
    position: absolute;
    left: 0;
    top: 0;
    width: 100%;
    height: 100%;
  }
  .footer-swoosh__band { fill: var(--teal); }
  .footer-swoosh__line { fill: none; stroke: var(--orange); stroke-width: 4; }
</style>
</head>
<body>
  <main class="canvas">
    <section class="envelope">
      <svg class="footer-swoosh" viewBox="0 0 1100 478" preserveAspectRatio="none" aria-hidden="true">
        <path class="footer-swoosh__band" d="M0,300 Q430,422 1100,468 L1100,478 L0,478 Z"/>
        <path class="footer-swoosh__line" d="M0,280 Q440,402 1100,456"/>
      </svg>
      <div class="return-address">
        <p class="club-name"><span class="club-name__dot"></span>Moravel Swim</p>
        <address class="address">418 West Harlan Ridge Road,<br>Corvell, PA 15592</address>
      </div>
    </section>
  </main>
</body>
</html>
```